Swing Dance Themed Cleaning Company Website

We need a website designed for a cleaning company based in Portland, Oregon called Bellhop Sweep. We clean homes and commercial buildings, inside and out.

needs to be vintage and like the velvet marlow. Speakeasy 1920s feel.
needs to be classy.

Check out bellhopsweep.com We are not happy with the site currently.

please look at house finderly site for more content https://www.housefinderly.com/rated.BellhopSweepCleaning.48217065.html

Check out my videos on my ClipHarbor channel Bellhop Sweep

Target Market(s)

middle class and home owner

Industry/Entity Type

Cleaning Service

Number of Pages Required

3 page

Font styles to use
Other font styles liked:
• jazzrag

Colors

Designer to choose colors to be used in the design.

Requirements
Must have
• must be good on pc and mobile

```html
<!DOCTYPE html>
<html lang="en">
<head>
<meta charset="utf-8">
<title>Bellhop Sweep – Portland Cleaning</title>
<link href="https://fonts.googleapis.com/css2?family=Merriweather:ital,wght@0,400;0,700;1,400&family=Raleway:wght@400;500;600&display=swap" rel="stylesheet">
<style>
:root{
  --gold:#a5835a;
  --gold-dark:#8c6c45;
  --ink:#333333;
  --muted:#777777;
  --line:#d9cbb8;
  --paper:#ffffff;
  --mist:#f1f1f1;
  --footer:#1f1f1f;
  --serif:"Merriweather", Georgia, serif;
  --sans:"Raleway", Arial, sans-serif;
}
*{box-sizing:border-box;margin:0;padding:0}
html,body{width:1200px;height:3636px;overflow:hidden}
body{font-family:var(--sans);color:var(--ink);background:var(--paper);position:relative}
section,header,footer{position:relative;width:1200px;overflow:hidden}

/* Hero */
.hero{height:589px}
.hero-photo{position:absolute;inset:0;background:linear-gradient(160deg,#6d6a68 0%,#8a8580 35%,#bfb7ab 60%,#7d776f 100%)}
.hero-shade{position:absolute;inset:0;background:rgba(40,32,26,.35)}
.brand{position:absolute;left:150px;top:24px;display:flex;align-items:center;gap:8px;color:#e6c15a;font-family:var(--serif);font-weight:700;font-size:15px;letter-spacing:.5px}
.brand-mark{width:22px;height:22px;background:#e6c15a}
.nav{position:absolute;top:34px;left:0;width:1200px;font-size:12px;color:#fff;font-weight:500}
.nav a{position:absolute;color:#fff;text-decoration:none;letter-spacing:.3px}
.hero-title{position:absolute;top:372px;width:100%;text-align:center;color:#fff;font-family:var(--serif);font-weight:700;font-size:26px;letter-spacing:1px}
.hero-sub{position:absolute;top:422px;width:100%;text-align:center;color:#fff;font-family:var(--serif);font-size:19px;letter-spacing:1px}
.btn-light{position:absolute;left:541px;top:462px;width:118px;height:36px;background:#e8e6e3;color:#444;font-family:var(--serif);font-size:12px;display:flex;align-items:center;justify-content:center}

/* Section heads */
.sec-title{position:absolute;width:100%;text-align:center;font-family:var(--serif);font-size:20px;color:var(--gold-dark);letter-spacing:1px}
.divider{position:absolute;left:540px;width:120px;height:10px}
.sec-sub{position:absolute;width:100%;text-align:center;font-size:12px;color:var(--muted)}

/* About */
.about{height:550px;border-left:2px solid var(--line);border-right:2px solid var(--line)}
.about-text{position:absolute;left:150px;width:450px;font-size:13px;line-height:21px;color:#444}
.about-text b{color:var(--gold-dark);font-family:var(--serif);font-weight:400}
.tagline{position:absolute;left:150px;top:349px;font-family:var(--serif);font-size:13px;color:var(--gold-dark)}
.btn{position:absolute;height:38px;display:flex;align-items:center;justify-content:center;font-family:var(--serif);font-size:12px}
.btn-outline{border:1px solid var(--gold);color:#333;background:#fff}
.btn-fill{background:var(--gold);color:#fff;border:1px solid var(--gold)}
.about-photo{position:absolute;left:740px;top:100px;width:300px;height:450px;background:linear-gradient(180deg,#e9eef5 0%,#b9c9de 45%,#5f7fa9 100%)}

/* Services */
.services{height:381px;display:flex}
.tile{position:relative;width:300px;height:381px;display:flex;align-items:center;justify-content:center;color:#fff;font-family:var(--serif);font-size:16px;letter-spacing:.5px}
.tile-janitorial{background:linear-gradient(150deg,#8a7566,#5a4a40)}
.tile-house{background:linear-gradient(160deg,#b9b1a8,#6b6259 60%,#4b8fb0)}
.tile-maintenance{background:linear-gradient(150deg,#2b2b2d,#4a4644 60%,#1d1d1f)}
.tile-event{background:radial-gradient(circle at 60% 40%,#c0587a,#3b4a8a 55%,#1e2248)}
.tile span{position:relative}
.tile-frame{position:absolute;left:20px;top:73px;width:252px;height:278px;border:1px solid rgba(255,255,255,.8);text-align:center;padding-top:44px}
.tile-frame h3{font-family:var(--serif);font-weight:400;font-size:16px;margin-bottom:14px}
.tile-frame p{font-family:var(--sans);font-size:13px;line-height:19px}
.tile-frame .btn{left:78px;top:176px;width:96px;height:34px;background:#f1f1f1;color:#333}

/* Why us */
.why{height:509px}
.feature{position:absolute;width:300px;text-align:center}
.icon-box{position:relative;width:140px;height:130px;margin:0 auto}
.icon-box .frame{position:absolute;border:1px solid #cfcfcf;width:124px;height:118px}
.icon-box .f1{left:0;top:0}
.icon-box .f2{left:14px;top:10px}
.icon-box svg{position:absolute;left:44px;top:38px}
.feature h4{font-family:var(--serif);font-weight:400;font-size:13px;color:var(--gold-dark);margin-top:62px;letter-spacing:.5px}
.feature p{font-size:11.5px;line-height:16px;color:#555;width:220px;margin:8px auto 0}

/* Blog */
.blog{height:524px;background:var(--mist)}
.card{position:absolute;top:111px;width:233px;height:328px;background:#fff;box-shadow:0 2px 6px rgba(0,0,0,.15)}
.card-photo{height:228px}
.card h5{font-family:var(--sans);font-weight:500;font-size:13.5px;line-height:19px;color:#333;padding:22px 12px 0}
.card .meta{font-family:var(--serif);font-size:11px;color:var(--gold-dark);padding:4px 12px 0}

/* Testimonials */
.testimonials{height:567px}
.quote-frame{position:absolute;left:162px;top:164px;width:589px;height:301px;border-top:2px solid var(--line);border-left:2px solid var(--line)}
.quote-base{position:absolute;left:250px;top:463px;width:501px;height:2px;background:var(--line)}
.quote-mark{position:absolute;left:698px;top:164px;font-family:var(--serif);font-size:80px;line-height:60px;color:var(--gold)}
.quote-head{position:absolute;left:205px;top:229px;font-family:var(--serif);font-size:12px;color:var(--gold-dark);letter-spacing:.3px}
.quote-body{position:absolute;left:205px;top:255px;width:520px;font-family:var(--serif);font-style:italic;font-size:12px;line-height:21px;color:#555}
.avatar{position:absolute;left:866px;top:231px;width:96px;height:96px;border-radius:50%;border:3px solid #e6e0d8;background:radial-gradient(circle,#c98d63,#7a5a44)}
.stars{position:absolute;left:832px;top:336px}
.person{position:absolute;left:780px;width:270px;text-align:center;font-family:var(--serif)}
.arrow{position:absolute;top:316px}
.dots{position:absolute;left:572px;top:512px;display:flex;gap:4px}
.dots i{width:9px;height:9px;border-radius:50%;border:1px solid #aaa;display:block}
.dots i.on{background:#aaa}

/* Reach out */
.reach{height:443px;color:#fff}
.reach-bg{position:absolute;inset:0;background:linear-gradient(120deg,#3f3c48 0%,#5d586c 45%,#6e6a80 100%)}
.reach h2{position:absolute;left:150px;top:34px;font-family:var(--serif);font-weight:400;font-size:22px;letter-spacing:1px}
.reach-text{position:absolute;left:150px;width:420px;font-size:12px;line-height:19px}
.contact{position:absolute;left:150px;display:flex;align-items:center;gap:18px;font-size:13px}
.field{position:absolute;left:606px;width:436px;height:32px;border:1px solid rgba(255,255,255,.6);font-size:11px;padding:9px 12px;color:#eee}
.field.msg{height:168px}
.submit{position:absolute;left:606px;top:380px;width:92px;height:36px;background:#f1f1f1;color:#333;font-family:var(--serif);font-size:12px;display:flex;align-items:center;justify-content:center}

/* Footer */
.footer{height:73px;background:var(--footer);color:#ddd;display:flex;align-items:center;justify-content:center;font-family:var(--serif);font-size:12px;letter-spacing:.5px}
</style>
</head>
<body>

<header class="hero">
  <div class="hero-photo" role="img" aria-label="Close-up of a vacuum cleaner head on a cream carpet"></div>
  <div class="hero-shade"></div>
  <div class="brand"><span class="brand-mark"></span>BELLHOP SWEEP</div>
  <nav class="nav">
    <a style="left:635px">HOME</a>
    <a style="left:703px">CONTACT US</a>
    <a style="left:810px">ABOUT US</a>
    <a style="left:902px">OUR SERVICES</a>
    <a style="left:1020px">BLOG</a>
  </nav>
  <h1 class="hero-title">BELLHOP SWEEP GET THE QUOTE TO DAY</h1>
  <p class="hero-sub">INDOOR – OURDOOR – CLASSIEST</p>
  <a class="btn-light">BOOK NOW</a>
</header>

<section class="about">
  <h2 class="sec-title" style="top:40px">ABOUT US</h2>
  <svg class="divider" style="top:63px" viewBox="0 0 120 10"><line x1="0" y1="5" x2="120" y2="5" stroke="#a5835a"/><rect x="56" y="1" width="8" height="8" transform="rotate(45 60 5)" fill="#a5835a"/></svg>
  <p class="sec-sub" style="top:80px">Making the greater Portland area clean, one building at a time</p>
  <p class="about-text" style="top:166px"><b>Bellhop Sweep</b> is a family owned professional cleaning business. We provide our years of cleaning experience to homes and businesses in and around Portland, Oregon. If you need something cleaned, have it cleaned the right way – contact us. Any doubts you have will be wiped away by our fantastic service and personable employees.</p>
  <p class="about-text" style="top:284px">Our most commonly performed services are listed here, but if you have a special project, let us know. We can clean just about anything!</p>
  <p class="tagline">GOOD PEOPLE – GREAT SERVICE</p>
  <a class="btn btn-outline" style="left:150px;top:402px;width:115px">READ MORE</a>
  <a class="btn btn-fill" style="left:273px;top:402px;width:115px">REVIEW</a>
  <div class="about-photo" role="img" aria-label="Cleaner in a blue apron holding a mop and a bucket of supplies"></div>
</section>

<section class="services">
  <div class="tile tile-janitorial" role="img" aria-label="Vacuum on a brown carpet"><span>JANITORIAL SERVICES</span></div>
  <div class="tile tile-house" role="img" aria-label="Mop cleaning a wooden floor"><span>HOUSE CLEANING</span></div>
  <div class="tile tile-maintenance" role="img" aria-label="Pressure washing a dark surface">
    <div class="tile-frame">
      <h3>MAINTENANCE</h3>
      <p>Pressure washing, Gutters,<br>Painting, Exterior windows,<br>Construction cleanup, Detailing</p>
      <a class="btn">READ MORE</a>
    </div>
  </div>
  <div class="tile tile-event" role="img" aria-label="Colourful lights at an evening event"><span>EVENT SERVICES</span></div>
</section>

<section class="why">
  <h2 class="sec-title" style="top:44px">WHY US ?</h2>
  <svg class="divider" style="top:70px" viewBox="0 0 120 10"><line x1="0" y1="5" x2="120" y2="5" stroke="#a5835a"/><rect x="56" y="1" width="8" height="8" transform="rotate(45 60 5)" fill="#a5835a"/></svg>
  <p class="sec-sub" style="top:88px">Nulla lacinia sollicitudin felis. Aliquam tortor magna</p>

  <div class="feature" style="left:92px;top:157px">
    <div class="icon-box"><div class="frame f1"></div><div class="frame f2"></div>
      <svg width="56" height="48" viewBox="0 0 56 48" fill="none" stroke="#8c6c45" stroke-width="2"><rect x="4" y="8" width="30" height="24"/><path d="M34 16h10l8 9v7H34z"/><circle cx="14" cy="36" r="5" fill="#fff"/><circle cx="42" cy="36" r="5" fill="#fff"/><line x1="0" y1="14" x2="10" y2="14"/><line x1="0" y1="20" x2="8" y2="20"/></svg>
    </div>
    <h4>FAST SERVICE</h4>
    <p>Lorem ipsum dolor sit amet, consectetur adipiscing elit. Duis rhoncus consequat est, vitae pretium nisl porta non. Duis</p>
  </div>
  <div class="feature" style="left:444px;top:157px">
    <div class="icon-box"><div class="frame f1"></div><div class="frame f2"></div>
      <svg width="56" height="48" viewBox="0 0 56 48" fill="none" stroke="#8c6c45" stroke-width="2"><circle cx="18" cy="16" r="9"/><circle cx="38" cy="16" r="9"/><path d="M4 46c0-10 6-16 14-16s14 6 14 16"/><path d="M24 46c0-10 6-16 14-16s14 6 14 16"/></svg>
    </div>
    <h4>FRIENDLY STAFF</h4>
    <p>Lorem ipsum dolor sit amet, consectetur adipiscing elit. Duis rhoncus consequat est, vitae pretium nisl porta non. Duis</p>
  </div>
  <div class="feature" style="left:790px;top:157px">
    <div class="icon-box"><div class="frame f1"></div><div class="frame f2"></div>
      <svg width="56" height="48" viewBox="0 0 56 48" fill="none" stroke="#8c6c45" stroke-width="2"><rect x="6" y="20" width="9" height="22"/><path d="M15 22l9-14c3-4 8-2 7 3l-2 9h12c3 0 5 3 4 6l-4 13c-1 2-3 3-5 3H15"/></svg>
    </div>
    <h4>HIGH QUALITY</h4>
    <p>Lorem ipsum dolor sit amet, consectetur adipiscing elit. Duis rhoncus consequat est, vitae</p>
  </div>
</section>

<section class="blog">
  <h2 class="sec-title" style="top:30px">OUR BLOG</h2>
  <svg class="divider" style="top:56px" viewBox="0 0 120 10"><line x1="0" y1="5" x2="120" y2="5" stroke="#a5835a"/><rect x="56" y="1" width="8" height="8" transform="rotate(45 60 5)" fill="#a5835a"/></svg>
  <article class="card" style="left:150px">
    <div class="card-photo" role="img" aria-label="Guitarist performing at an outdoor festival" style="background:linear-gradient(160deg,#9fa184,#6b4a3a 55%,#b34a3e)"></div>
    <h5>Bellhop Sweep Returns to Riverside Rhythm Festival 2017</h5>
    <p class="meta">READ MORE | JULY 25/2017</p>
  </article>
  <article class="card" style="left:483px">
    <div class="card-photo" role="img" aria-label="Festival guest in a colourful hat" style="background:linear-gradient(160deg,#d8a04a,#c65a7a 50%,#7bb0c8)"></div>
    <h5>Bellhop Sweep sponsoring Riverside Rhythm Fest 2016</h5>
    <p class="meta">READ MORE | JULY 25/2016</p>
  </article>
  <article class="card" style="left:815px">
    <div class="card-photo" role="img" aria-label="Crowd gathered under festival lights" style="background:linear-gradient(170deg,#8a7a68,#4e3a30 60%,#2e2622)"></div>
    <h5>Bellhop Sweep Returns to Riverside Rhythm Festival 2017</h5>
    <p class="meta">READ MORE | JULY 25/2017</p>
  </article>
</section>

<section class="testimonials">
  <h2 class="sec-title" style="top:36px">CLIENT TESTIMONIALS</h2>
  <svg class="divider" style="top:60px" viewBox="0 0 120 10"><line x1="0" y1="5" x2="120" y2="5" stroke="#a5835a"/><rect x="56" y="1" width="8" height="8" transform="rotate(45 60 5)" fill="#a5835a"/></svg>
  <p class="sec-sub" style="top:76px">see what our clients ay about us.</p>
  <div class="quote-frame"></div>
  <div class="quote-base"></div>
  <div class="quote-mark">&rdquo;</div>
  <p class="quote-head">THIS IS THE BEST SERVICE I'VE USED SO FAR</p>
  <p class="quote-body">Vivamus a faucibus mauris. Praesent maximus porttitor justo eu faucibus. Suspendisse vitae rutrum arcu. Maecenas vel blandit sapien. Vestibulum nisl lectus, consectetur scelerisque ante id, cursus dignissim dui. Nam elit urna, semper quis odio et, dictum pellentesque leo. Maecenas quis sagittis nibh. Quisque consectetur sem nec euismod rutrum. Vestibulum eu rutrum nisi, at iaculis massa. Duis pellentesque lacinia finibus. Praesent tortor massa, rutrum id volutpat vitae, interdum in ipsum.</p>
  <div class="avatar" role="img" aria-label="Portrait of the client"></div>
  <svg class="stars" width="165" height="22" viewBox="0 0 165 22" fill="#8c6c45">
    <g id="star"><polygon points="11,1 14,8 21,8.5 15.5,13 17.5,20 11,16 4.5,20 6.5,13 1,8.5 8,8"/></g>
    <use href="#star" x="36"/><use href="#star" x="72"/><use href="#star" x="108"/><use href="#star" x="144"/>
  </svg>
  <p class="person" style="top:373px;font-size:15px;color:#555">Lou B. Hartwell</p>
  <p class="person" style="top:400px;font-size:11px;color:#777">Henry Ashcombe &amp; Sons</p>
  <svg class="arrow" style="left:72px" width="16" height="30" viewBox="0 0 16 30"><polyline points="14,2 2,15 14,28" fill="none" stroke="#bbb" stroke-width="2"/></svg>
  <svg class="arrow" style="left:1110px" width="16" height="30" viewBox="0 0 16 30"><polyline points="2,2 14,15 2,28" fill="none" stroke="#bbb" stroke-width="2"/></svg>
  <div class="dots"><i class="on"></i><i></i><i></i><i></i></div>
</section>

<section class="reach">
  <div class="reach-bg" role="img" aria-label="Vacuum cleaner on a carpet in muted purple tones"></div>
  <h2>REACH OUT</h2>
  <p class="reach-text" style="top:84px">We have a flexible team ready to meet your cleaning needs, servicing Multnomah, Washington, and Clackamas Counties. Offering cleaning, janitorial, and maintenance services for your home, apartment or business, we provide both one-time as well as weekly, bi-weekly or monthly cleaning services.</p>
  <p class="reach-text" style="top:200px">If you're ready to experience a professional cleaning, reach out to us now!</p>
  <div class="contact" style="top:268px">
    <svg width="18" height="18" viewBox="0 0 24 24" fill="#fff"><path d="M6.6 10.8a15 15 0 006.6 6.6l2.2-2.2c.3-.3.7-.4 1-.2 1.1.4 2.3.6 3.6.6.6 0 1 .4 1 1V20c0 .6-.4 1-1 1A17 17 0 013 4c0-.6.4-1 1-1h3.5c.6 0 1 .4 1 1 0 1.3.2 2.5.6 3.6.1.3 0 .7-.2 1z"/></svg>
    <span>971-555-0148</span>
  </div>
  <div class="contact" style="top:304px">
    <svg width="18" height="18" viewBox="0 0 24 24" fill="#fff"><path d="M12 2a7 7 0 00-7 7c0 5 7 13 7 13s7-8 7-13a7 7 0 00-7-7zm0 9.5A2.5 2.5 0 1112 6.5a2.5 2.5 0 010 5z"/></svg>
    <span>418 SE Alder St #210, Portland, OR 97214</span>
  </div>
  <div class="contact" style="top:340px">
    <svg width="18" height="18" viewBox="0 0 24 24" fill="#fff"><path d="M2 11l20-9-7 20-3-8z"/></svg>
    <span>robert@bellhopsweep.com</span>
  </div>
  <div class="field" style="top:32px">Name</div>
  <div class="field" style="top:84px">Email</div>
  <div class="field" style="top:136px">Request a quote</div>
  <div class="field msg" style="top:180px">Message</div>
  <a class="submit">SUBMIT</a>
</section>

<footer class="footer">COPY RIGHT 2018 BELLHOP SWEEP.</footer>

</body>
</html>
```